Zielgruppe
Hausarztpraxis Dr. Wildhagen
Patientenbetreuung / Junge Patienten
Aufgabenstellung
Bitte Mit dem Praxis Logo. Gern auch ein Foto aus der Praxis. In den Farben der Praxis Weiß-Magenta-Grau
Es soll kein Newsletter an sich werden, sondern eine Email die die Patienten nach Ihrem Besuch in der Praxis bekommen. Dort soll dann die Suchflixseite verlinkt sein mit einem Button zum bewerten!

```html
<!DOCTYPE html>
<html lang="de">
<head>
<meta charset="utf-8">
<title>Ihre Meinung ist uns wichtig – Hausarztpraxis Dr. Wildhagen</title>
<link href="https://fonts.googleapis.com/css2?family=Open+Sans:wght@400;600&display=swap" rel="stylesheet">
<style>
  :root {
    --magenta: #c41a55;
    --magenta-soft: rgba(196, 26, 85, 0.8);
    --pink-band: #ef6a9c;
    --text-grey: #5a5a5a;
    --white: #ffffff;
    --photo-light: #eeeceb;
    --photo-mid: #c9c4bf;
    --photo-dark: #8f8780;
  }
  * { margin: 0; padding: 0; box-sizing: border-box; }
  html, body { width: 1200px; height: 1139px; overflow: hidden; background: var(--white); }
  body { position: relative; font-family: "Open Sans", Arial, sans-serif; color: var(--text-grey); }

  .brand { position: absolute; top: 25px; left: 0; width: 1200px; text-align: center; }
  .brand-dot { display: block; width: 62px; height: 62px; margin: 0 auto; border-radius: 50%; background: var(--magenta); }
  .brand-name { margin-top: 16px; font-size: 20px; font-weight: 600; color: var(--magenta); letter-spacing: 0.5px; }

  .hero-photo { position: absolute; top: 182px; left: 0; width: 1200px; height: 336px;
    background: linear-gradient(90deg, var(--photo-light) 0%, #f3f2f1 40%, var(--photo-mid) 62%, #b8b2ad 80%, var(--photo-dark) 100%); }

  .hero-pill { position: absolute; top: 431px; left: 260px; width: 680px; height: 151px; border-radius: 76px;
    background: var(--magenta-soft); color: var(--white); text-align: center; padding-top: 33px; }
  .hero-title { font-size: 35px; font-weight: 400; line-height: 44px; }
  .hero-sub { margin-top: 8px; font-size: 15.5px; line-height: 20px; }

  .message { position: absolute; top: 629px; left: 260px; width: 680px; text-align: center; font-size: 14.5px; line-height: 18.75px; }
  .message p + p { margin-top: 18.75px; }

  .rate-button { position: absolute; top: 833px; left: 476px; width: 248px; height: 41px; border-radius: 21px;
    background: var(--magenta); color: var(--white); font-size: 16px; line-height: 41px; text-align: center; text-decoration: underline; }

  .closing { position: absolute; top: 911px; left: 200px; width: 800px; text-align: center; font-size: 14.5px; line-height: 18.75px; }
  .closing p + p { margin-top: 18.75px; }

  .footer-band { position: absolute; top: 1095px; left: 0; width: 1200px; height: 12px; background: var(--pink-band); }
  .footer { position: absolute; top: 1107px; left: 0; width: 1200px; height: 32px; background: var(--magenta);
    color: var(--white); text-align: center; font-size: 13.5px; line-height: 32px; }
  .footer a { color: var(--white); text-decoration: none; }
</style>
</head>
<body>
  <header class="brand">
    <span class="brand-dot"></span>
    <div class="brand-name">Hausarztpraxis Dr. med. Wendelin Wildhagen</div>
  </header>

  <div class="hero-photo" role="img" aria-label="Foto des hellen Wartebereichs der Praxis mit weißen Stühlen, Bambus-Raumteiler und grauen Sesseln"></div>

  <section class="hero-pill">
    <h1 class="hero-title">Ihre Meinung ist uns wichtig.</h1>
    <p class="hero-sub">Nehmen Sie sich kurz zeit und bewerten Sie uns auf Suchflix.</p>
  </section>

  <section class="message">
    <p>Liebe Patientin, Lieber Patient,</p>
    <p>wie war Ihre Erfahrung in unserer Praxis?</p>
    <p>Wir versuchen uns ständig zu verbessern und freuen uns, wenn Sie uns ein kurzes Feedback geben würden. Es Wäre toll, wenn Sie sich kurz die Zeit nehmen um eine Bewertung bei Suchflix zu schreiben, denn damit hilfst du uns und auch anderen Patienten uns zu finden.</p>
    <p>Um Ihre Bewertung zu schreiben und abzuschicken genügt ein Klick!</p>
  </section>

  <a class="rate-button" href="#">Hier bewerten</a>

  <section class="closing">
    <p>Vielen Dank im Voraus für Ihre Bewertung!<br>Bei Fragen oder falls Sie uns erneut besuchen möchten, stehen wir Ihnen gern jederzeit zur Verfügung!</p>
    <p>Melden Sie sich gern unter der 07041 - 5820 oder wieder über unseren<br>Online Terminkalender der Website.</p>
    <p>Vielen Grüße<br>Ihr Praxisteam Dr. Wildhagen</p>
  </section>

  <div class="footer-band"></div>
  <footer class="footer">
    <a href="#">Impressum</a>&nbsp; I <a href="#">Datenschutz</a> I <a href="#">Unsere Praxis</a> I <a href="#">Kontakt</a>
  </footer>
</body>
</html>
```